ashby paving works

Needs to have phone number 0412885107 and email marklowry@pavemail.com.au.
ABN 27613048852
name mark lowry

For all your concreting solutions
Excavation
Exposed & colour concrete
House & shed slabs
Driveways
Landing & steps

Contact Information for Business Card

ph 0412885107
email marklowry@pavemail.com.au.
ABN 27613048852
name mark lowry

```html
<!DOCTYPE html>
<html lang="en">
<head>
<meta charset="utf-8">
<title>Ashby Paving Works – Business Card</title>
<link rel="stylesheet" href="https://fonts.googleapis.com/css2?family=Montserrat:wght@700&family=Open+Sans:wght@400;600&display=swap">
<style>
  :root {
    --bg: #3a3330;
    --card: #151516;
    --orange: #ec6a2c;
    --grey: #6b6b6b;
    --text: #e9e9e9;
    --muted: #c9c9c9;
  }
  * { margin: 0; padding: 0; box-sizing: border-box; }
  html, body { width: 1200px; height: 864px; overflow: hidden; }
  body {
    background: var(--bg);
    font-family: "Open Sans", Arial, sans-serif;
    position: relative;
  }
  .card {
    position: absolute;
    top: 274px;
    width: 550px;
    height: 316px;
    background: var(--card);
    box-shadow: 0 10px 30px rgba(0,0,0,.45);
    overflow: hidden;
  }
  .card--services { left: 35px; }
  .card--contact { left: 615px; }

  .brand {
    position: absolute;
    display: flex;
    align-items: center;
    gap: 14px;
    white-space: nowrap;
  }
  .brand__mark {
    width: 34px; height: 34px;
    background: var(--grey);
    flex: none;
  }
  .brand__divider {
    width: 2px; height: 62px;
    background: var(--orange);
    flex: none;
  }
  .brand__name {
    font-family: "Montserrat", Arial, sans-serif;
    font-weight: 700;
    color: var(--orange);
    font-size: 17px;
    line-height: 1.15;
    text-transform: uppercase;
    letter-spacing: .3px;
  }
  .brand__phone {
    font-family: "Montserrat", Arial, sans-serif;
    font-weight: 700;
    color: var(--orange);
    font-size: 15px;
    letter-spacing: 1px;
    margin-top: 4px;
    padding-top: 3px;
    border-top: 2px solid var(--grey);
  }

  .card--services .brand { left: 50%; top: 62px; transform: translateX(-50%); }
  .services {
    position: absolute;
    left: 0; right: 0; top: 196px;
    text-align: center;
    color: var(--muted);
    font-size: 14.5px;
    line-height: 1.7;
  }
  .services .dot { color: var(--text); margin: 0 4px; }

  .card--contact .brand { right: 40px; top: 52px; }
  .holder {
    position: absolute;
    left: 40px; top: 152px;
    font-weight: 600;
    color: var(--orange);
    font-size: 18px;
    text-transform: uppercase;
  }
  .contact-list {
    position: absolute;
    left: 40px; top: 184px;
    list-style: none;
    color: var(--text);
    font-size: 14px;
    line-height: 1.55;
  }
  .contact-list li { display: flex; align-items: center; gap: 8px; }
  .contact-list svg { width: 12px; height: 12px; flex: none; }
  .rule {
    position: absolute;
    left: 40px; right: 40px; top: 256px;
    height: 1px;
    background: var(--text);
  }
  .abn {
    position: absolute;
    right: 40px; top: 270px;
    color: var(--text);
    font-size: 14.5px;
  }
</style>
</head>
<body>

<section class="card card--services">
  <div class="brand">
    <span class="brand__mark"></span>
    <span class="brand__divider"></span>
    <div>
      <div class="brand__name">Ashby Paving Works</div>
      <div class="brand__phone">0412885107</div>
    </div>
  </div>
  <p class="services">
    Excavation <span class="dot">•</span> Exposed &amp; colour concrete<br>
    House &amp; shed slabs <span class="dot">•</span> Driveways <span class="dot">•</span> Landing &amp; steps
  </p>
</section>

<section class="card card--contact">
  <div class="brand">
    <span class="brand__mark"></span>
    <span class="brand__divider"></span>
    <div>
      <div class="brand__name">Ashby Paving Works</div>
      <div class="brand__phone">0412885107</div>
    </div>
  </div>

  <h1 class="holder">Mark Lowry</h1>
  <ul class="contact-list">
    <li>
      <svg viewBox="0 0 12 12" aria-hidden="true"><path fill="#ec6a2c" d="M2.5 1h2l1 2.5-1.3 1a6 6 0 0 0 3.3 3.3l1-1.3L11 7.5v2A1.5 1.5 0 0 1 9.5 11 8.5 8.5 0 0 1 1 2.5 1.5 1.5 0 0 1 2.5 1z"/></svg>
      0412885107
    </li>
    <li>
      <svg viewBox="0 0 12 12" aria-hidden="true"><rect x="0.5" y="2.5" width="11" height="7.5" rx="1" fill="#ec6a2c"/><path d="M1 3l5 3.5L11 3" stroke="#151516" stroke-width="1" fill="none"/></svg>
      marklowry@pavemail.com.au
    </li>
    <li>
      <svg viewBox="0 0 12 12" aria-hidden="true"><circle cx="6" cy="6" r="5.5" fill="#ec6a2c"/><circle cx="6" cy="6" r="2" fill="#151516"/></svg>
      www.ashbypaving.com.au
    </li>
  </ul>
  <div class="rule"></div>
  <p class="abn">ABN 27613048852</p>
</section>

</body>
</html>
```